Business Card design for amazing new Dental Office

Please read this brief closely!

Our client is a modern new dental office/
They love their new logo.
Now it's time to create a business card for them.

It should be a two sided card:
Side one should have the logo and name and maybe a color background or design.
Side two should have all the contact information which is here:

Marcus Holloway, D.D.S
General and Cosmetic Dentistry
4187 W. Pinecrest Avenue
Ventura, CA 93011
(805) 912-4386
drmarcus@bluefernsmiles-example.com
www.bluefernsmiles-example.com

Feel free to arrange that info as you like and to style both sides of the card according to your creativity. This is a chance for you to show your design skills!

Client is open to font choices and is looking for a style that is amazing and premium. Colors can be selected from the logo, or any variation of those.

You will not win this contest with a less than beautiful card design so please feel free to make multiple submissions.

Logo files attached and please message me with any questions.
Thanks!

Target Market(s)

Families and Professionals seeking dental services

Industry/Entity Type

Dental

Contact Information for Business Card

Logo, style, contact info as per the brief

Font styles to use
Sans Serif

Requirements
Must have
• Client's logo and contact details as per brief
Nice to have
• Unique style reflecting high end dental clinic near the beach
Should not have
• Must not look like a template

```html
<!DOCTYPE html>
<html lang="en">
<head>
<meta charset="utf-8">
<title>Blue Fern Smiles – Business Card</title>
<link rel="stylesheet" href="https://fonts.googleapis.com/css2?family=Jost:wght@300&family=Poppins:wght@400;600&display=swap">
<style>
  :root {
    --stage: #c9c6c3;
    --paper-light: #fbfbfb;
    --paper-dark: #e4e4e4;
    --sea-light: #64998a;
    --sea-dark: #467567;
    --ink-grey: #868686;
    --ink-soft: #9a9a9a;
    --white: #ffffff;
  }
  * { box-sizing: border-box; margin: 0; padding: 0; }
  html, body { width: 1200px; height: 1200px; overflow: hidden; }
  body {
    background: var(--stage);
    position: relative;
    font-family: "Poppins", sans-serif;
  }
  .card {
    position: absolute;
    left: 243px;
    width: 702px;
    height: 400px;
    border-radius: 19px;
    overflow: hidden;
  }
  .card-front {
    top: 170px;
    background: linear-gradient(225deg, var(--paper-dark), var(--paper-light) 70%);
  }
  .card-back {
    top: 630px;
    background: linear-gradient(160deg, var(--sea-light), var(--sea-dark));
  }
  .card svg.shape { position: absolute; inset: 0; }
  .brand-name {
    position: absolute;
    font-family: "Jost", sans-serif;
    font-weight: 300;
    white-space: nowrap;
  }
  .card-front .brand-name {
    left: 351px; top: 204px;
    transform: translateX(-50%);
    font-size: 28px;
    letter-spacing: 3px;
    color: var(--ink-soft);
  }
  .card-back .brand-name {
    right: 30px; top: 106px;
    font-size: 22px;
    letter-spacing: 2px;
    color: var(--white);
  }
  .person {
    position: absolute;
    left: 33px; top: 30px;
  }
  .person-name {
    font-weight: 600;
    font-size: 21px;
    color: var(--ink-grey);
    letter-spacing: -0.2px;
  }
  .person-role {
    font-size: 16px;
    line-height: 20px;
    color: var(--ink-grey);
    margin-top: 2px;
  }
  .contacts {
    position: absolute;
    left: 34px; top: 305px;
    list-style: none;
    color: var(--white);
    font-size: 16px;
    line-height: 23.5px;
  }
  .contacts li { display: flex; align-items: center; gap: 12px; }
  .contacts svg { width: 16px; height: 16px; flex: none; }
  .address {
    position: absolute;
    right: 28px; top: 316px;
    text-align: right;
    color: var(--white);
    font-size: 18px;
    line-height: 23px;
    font-style: normal;
  }
</style>
</head>
<body>

<section class="card card-front">
  <svg class="shape" width="702" height="400" viewBox="0 0 702 400" aria-hidden="true">
    <path fill="var(--sea-dark)" d="M481 400 c18 -2 22 -26 44 -28 c18 -2 22 -26 44 -28 c18 -2 22 -26 44 -28 c18 -2 22 -26 44 -28 c18 -2 22 -26 44 -28 L702 400 Z"/>
  </svg>
  <div class="brand-name">BLUE FERN SMILES</div>
</section>

<section class="card card-back">
  <svg class="shape" width="702" height="400" viewBox="0 0 702 400" aria-hidden="true">
    <defs>
      <linearGradient id="paperSide" x1="0" y1="0" x2="1" y2="1">
        <stop offset="0" stop-color="#f6f6f6"/>
        <stop offset="1" stop-color="#ebebeb"/>
      </linearGradient>
    </defs>
    <path fill="url(#paperSide)" d="M0 0 H409 c-22 2 -29 31 -51 33 c-22 2 -29 31 -51 33 c-22 2 -29 31 -51 33 c-22 2 -29 31 -51 33 c-22 2 -29 31 -51 33 c-22 2 -29 31 -51 33 c-22 2 -29 31 -51 33 c-22 2 -29 31 -51 33 L0 264 Z"/>
  </svg>

  <div class="person">
    <h1 class="person-name">Marcus Holloway, D.D.S</h1>
    <p class="person-role">General and<br>Cosmetic Dentistry</p>
  </div>

  <div class="brand-name">BLUE FERN SMILES</div>

  <ul class="contacts">
    <li>
      <svg viewBox="0 0 24 24" aria-hidden="true"><path fill="#fff" d="M6.6 10.8a15.1 15.1 0 0 0 6.6 6.6l2.2-2.2a1 1 0 0 1 1-.25 11.4 11.4 0 0 0 3.6.57 1 1 0 0 1 1 1V20a1 1 0 0 1-1 1A17 17 0 0 1 3 4a1 1 0 0 1 1-1h3.5a1 1 0 0 1 1 1c0 1.25.2 2.45.57 3.57a1 1 0 0 1-.25 1z"/></svg>
      (805) 912-4386
    </li>
    <li>
      <svg viewBox="0 0 24 24" aria-hidden="true"><path fill="#fff" d="M2 5h20v14H2z"/><path fill="none" stroke="var(--sea-light)" stroke-width="1.8" d="M2.5 5.5 12 13l9.5-7.5"/></svg>
      drmarcus@bluefernsmiles-example.com
    </li>
    <li>
      <svg viewBox="0 0 24 24" aria-hidden="true"><g fill="none" stroke="#fff" stroke-width="2"><circle cx="12" cy="12" r="9.5"/><ellipse cx="12" cy="12" rx="4" ry="9.5"/><path d="M2.5 12h19"/></g></svg>
      www.bluefernsmiles-example.com
    </li>
  </ul>

  <address class="address">
    4187 W. Pinecrest Avenue<br>
    Ventura, CA 93011
  </address>
</section>

</body>
</html>
```